Visitenkarten-Design für Immobilienmakler
Zielgruppe
Immobilienmakler
Aufgabenstellung
Top moderne hochwertige Visitenkate, wir hätten gerne eine sehr hochwertig moderne Visitenkarte mit Bild vom Mitarbeiter... Anbei habe ich die alte Visitenkarte die ich sehr kindlich finde... Es sollte jetzt sehr exklusive aussehen. Alle Daten können von der alten Visitenkarte übernommen werden.. danke

```html
<!DOCTYPE html>
<html lang="de">
<head>
<meta charset="utf-8">
<title>Visitenkarte – Lukas Brenner</title>
<link rel="stylesheet" href="https://fonts.googleapis.com/css2?family=Crimson+Pro:wght@400;600&display=swap">
<style>
  :root {
    --card-bg: #1c1c1c;
    --ink-light: #ffffff;
    --ink-muted: #bcbcbc;
    --ink-footer: #b0b0b0;
    --divider: #6a6a6a;
    --portrait-light: #f2f2f2;
    --portrait-mid: #bdbdbd;
  }
  * { margin: 0; padding: 0; box-sizing: border-box; }
  html, body {
    width: 1200px; height: 796px; overflow: hidden;
    background: var(--card-bg);
  }
  .card {
    position: relative;
    width: 1200px; height: 796px;
    background: var(--card-bg);
    font-family: "Crimson Pro", Georgia, serif;
    color: var(--ink-light);
  }
  .portrait {
    position: absolute;
    left: 450px; top: 76px;
    width: 300px; height: 300px;
  }
  .name {
    position: absolute; left: 0; right: 0; top: 382px;
    text-align: center;
    font-size: 48px; font-weight: 600; line-height: 1;
  }
  .role {
    position: absolute; left: 0; right: 0; top: 456px;
    text-align: center;
    font-size: 45px; font-weight: 400; line-height: 1;
    letter-spacing: 0.3px;
  }
  .contact {
    position: absolute; top: 528px; left: 116px;
    display: grid;
    grid-template-columns: 535px auto;
    row-gap: 14px;
    font-size: 40px; line-height: 40px;
    color: var(--ink-muted);
    white-space: nowrap;
  }
  .divider {
    position: absolute; left: 0; right: 0; top: 661px;
    height: 2px; background: var(--divider);
  }
  .address {
    position: absolute; left: 0; right: 0; top: 698px;
    text-align: center;
    font-size: 37px; line-height: 1;
    color: var(--ink-footer);
    word-spacing: 2px;
  }
  .address .sep { margin: 0 14px; }
</style>
</head>
<body>
  <div class="card">
    <svg class="portrait" viewBox="0 0 300 300" role="img" aria-label="Porträtfoto des Mitarbeiters in Schwarzweiß">
      <defs>
        <radialGradient id="portraitTone" cx="50%" cy="45%" r="60%">
          <stop offset="0%" stop-color="var(--portrait-light)"/>
          <stop offset="100%" stop-color="var(--portrait-mid)"/>
        </radialGradient>
      </defs>
      <circle cx="150" cy="150" r="147" fill="none" stroke="var(--ink-light)" stroke-width="2.5"/>
      <circle cx="150" cy="150" r="141" fill="url(#portraitTone)"/>
    </svg>

    <h1 class="name">Lukas Brenner</h1>
    <p class="role">Dipl. Immobilienmanager &amp; Geschäftsführer</p>

    <div class="contact">
      <span class="phone">Telefon +43 5500 12 345 67</span>
      <span class="mobile">Mobil +43 660 4820 917</span>
      <span class="email">lukas@velmar-agentur.com</span>
      <span class="web">www.velmar-agentur.com</span>
    </div>

    <div class="divider"></div>

    <p class="address">Velmar Agentur<span class="sep">|</span>Am Feldweg 4<span class="sep">|</span>6800 Musterau</p>
  </div>
</body>
</html>
```